Trellopace.com a website for sport coaches and their students...

Trellopace.com is a online portal for sport coaches. It was originally created for golf teaching professionals. We want to not restrict to only golf and want to have a website that attract coaches in all sports as well as students in all sports. We believe that students are as important as coaches and believe that we can make a good business with the students rather than with the coaches. The coaches are the marketing generator as they bring the students to the platform.The following functionality we offer at the moment:Online BookingTraining DiaryStudent organisationOnline lessonsTeam training.ics CalendarOnline paymentVoucher ManagementVideo tips from the best coachesTraining goal platformWhat I would like to get changed is the front page. It needs to be really easy and possible to reach both students and coaches. It needs to attract the audience with features that are presented in a good way for them to join the portal. I also want to change the dashboard which is currently build with building blocks. In a way very easy but if I want to get the user to get hungry for material or pay for new material such as new video tips or online lesson or team training or general news that we can keep feeding them with I would like to show that in the dashboard somehow...The website is live and is called Trellopace.com. the front page is the first thing I would like to get changed. It all used to be in green color as we first used it for Golf only and then the green color was good. now we would like to change it and then the logo color is a bit outdated...The dashboard: here I would like to get an idea of how to get it to be easy to navigate to other screens and also to maybe make the building blocks more nicer looking...
Updates

I see that the screens that are being submitted are not quite fulfilling the needs. The front page should include a picture that do not only restrict the portal to golf but rather multiple sports...I also asked to get example of the dashboard as I still find the dashboard not looking sexy enough...(dashboard is the screen with the blocks)... For some I got a logo update but not for all...so a nice logo update would be nice for those who have not provided it. The color of the homepage should not be too dark but rather a more lighter color...The reason for this blue background color with the shaded sports athlete in the background was to illustrate that it is for multiple sports and not only golf...If you have another suggestion how to illustrate this I am open...

Target Market(s)

All sports

Logo Text

trellopace.com (slogan should be "get better" I think or maybe there is something better if you find something) important is that the student can get to the portal to get a feeling that he or she can get better by using trellopace.com

Number of Pages Required

2 page

Requirements
Must have
• what do we want for customers? a happy in style golfer/student who wants to have a good time learning golf/or any other sport, hit longer make more puts etc. friendly atmosphere friendly light color not stressy but sexy motivating…
• I would like to have the homepage done and also a reworked dashboard...
• The homepage should include a picture that have more sports and not just golf...golf should be part of the sports shown but we need to reach out to more sports and not restrict it to golf...
Nice to have
• On the front page I would like to see something like a site I saw vondurix.com...
• It is only for golf but the explanation they do it quite nice...
Should not have
• not to restrict it to only golf....The first picture on the homepage should not include a golf pls...

```html
<!DOCTYPE html>
<html lang="en">
<head>
<meta charset="utf-8">
<title>Trellopace – Home</title>
<link href="https://fonts.googleapis.com/css2?family=Fira+Sans:wght@300;400;500;600;700&family=Arimo:wght@400;700&display=swap" rel="stylesheet">
<style>
  :root{
    --backdrop:#333333;
    --page:#ffffff;
    --lime:#8dc63f;
    --forest:#15692f;
    --orange:#ea6b2e;
    --blue:#0a78c2;
    --red:#d9322a;
    --yellow:#fbc12e;
    --taupe:#8f8480;
    --sand:#ddd7c9;
    --footer:#2c2c2c;
    --ink:#222222;
    --muted:#6a6a6a;
  }
  *{box-sizing:border-box;margin:0;padding:0}
  html,body{width:1200px;height:1200px;overflow:hidden}
  body{background:var(--backdrop);font-family:"Arimo",Arial,sans-serif;color:var(--ink);position:relative}
  .page{position:absolute;left:226px;top:24px;width:749px;height:1152px;background:var(--page);overflow:hidden}
  .abs{position:absolute}

  /* header */
  .brand{position:absolute;left:45px;top:24px;display:flex;align-items:center;gap:5px}
  .brand-dot{width:22px;height:22px;border-radius:50%;background:var(--lime)}
  .brand-name{font-family:"Fira Sans",sans-serif;font-weight:600;font-size:24px;color:var(--lime);letter-spacing:-.5px;line-height:1}
  .nav{position:absolute;left:319px;top:26px;display:flex;align-items:center;font-family:"Arimo",sans-serif;font-size:8px;color:var(--muted)}
  .nav a{text-decoration:none;color:inherit;padding:0 8px;line-height:20px}
  .nav a.active{background:var(--lime);color:#fff;font-weight:700;border-radius:3px;padding:0 11px}

  /* hero */
  .hero{position:absolute;left:0;top:66px;width:749px;height:235px;display:flex}
  .hero-panel{height:100%}
  .arrow{position:absolute;top:171px;width:24px;height:24px}

  /* band */
  .band{position:absolute;left:0;top:301px;width:749px;height:77px;background:var(--lime)}
  .band-copy{position:absolute;right:350px;top:22px;text-align:right;color:#fff;font-family:"Fira Sans",sans-serif;line-height:19px}
  .band-copy .l1{font-weight:300;font-size:16px}
  .band-copy .l2{font-weight:600;font-size:14px}
  .btn{position:absolute;display:flex;align-items:center;justify-content:center;font-family:"Fira Sans",sans-serif;border-radius:3px;color:#fff}
  .btn-book{left:414px;top:326px;width:104px;height:29px;background:var(--forest);font-size:13px;font-weight:500}
  .btn-cal{left:530px;top:326px;width:105px;height:29px;background:var(--orange);font-size:10.5px;font-weight:500}

  /* video tips */
  .tips-title{position:absolute;left:47px;top:436px;font-family:"Fira Sans",sans-serif}
  .tips-title .kicker{font-weight:300;font-size:19px;color:var(--muted);line-height:22px}
  .tips-title .head{font-weight:700;font-size:29px;color:var(--forest);line-height:32px}
  .tips-text{position:absolute;left:47px;top:500px;font-size:7px;line-height:13px;color:var(--ink);white-space:nowrap}
  .btn-more{font-family:"Fira Sans",sans-serif;font-weight:500;font-size:9px;border-radius:2px}
  .btn-more.green{position:absolute;left:47px;top:567px;width:74px;height:20px;background:var(--forest);color:#fff;display:flex;align-items:center;justify-content:center}

  /* feature grid */
  .grid{position:absolute;left:45px;top:713px;width:659px;height:296px;display:grid;grid-template-columns:repeat(4,1fr);grid-template-rows:repeat(2,1fr)}
  .tile{position:relative;padding:20px 18px 0}
  .tile h3{font-family:"Arimo",sans-serif;font-weight:700;font-size:12px;line-height:12px;margin-bottom:12px}
  .tile p{font-size:6.6px;line-height:11.5px;white-space:nowrap}
  .tile .btn-more{position:absolute;left:18px;bottom:22px;width:74px;height:20px;background:#fff;color:var(--ink);display:flex;align-items:center;justify-content:center;font-weight:600}
  .t-red{background:var(--red);color:#fff}
  .t-yellow{background:var(--yellow);color:var(--ink)}
  .t-yellow h3{margin-top:4px}
  .t-taupe{background:var(--taupe);color:#fff}
  .t-sand{background:var(--sand);color:#6b655c}
  .t-sand h3{font-weight:400;font-size:12px;line-height:12px;color:#6b655c}
  .t-sand p{color:#7a746b}

  /* footer */
  .footer{position:absolute;left:0;top:1054px;width:749px;height:98px;background:var(--footer)}
  .fcol{position:absolute;top:31px;font-size:8.5px;line-height:14.5px;color:#cfcfcf}
  .fcol h4{font-weight:400;color:var(--lime);font-size:8.5px;line-height:14.5px}
  .social{position:absolute;top:43px;width:24px;height:24px;border:1.5px solid #555;border-radius:50%}
</style>
</head>
<body>
<div class="page">

  <header>
    <div class="brand"><span class="brand-dot"></span><span class="brand-name">trellopace</span></div>
    <nav class="nav">
      <a class="active">Home</a><a>Calendar</a><a>Online Lessons</a><a>My Products</a><a>Students</a><a>My Offers</a><a>Trellopace 365</a>
    </nav>
  </header>

  <section class="hero">
    <div class="hero-panel" style="width:117px;background:linear-gradient(160deg,#d9ddd8,#6a6f5e 70%,#3e4434)" role="img" aria-label="Rugby players leaping for a ball in a lineout"></div>
    <div class="hero-panel" style="width:128px;background:linear-gradient(180deg,#cfd6d0 0%,#8fa36a 45%,#3f7a1f 100%)" role="img" aria-label="Golfer on a sunlit green beside the hole"></div>
    <div class="hero-panel" style="width:128px;background:linear-gradient(180deg,#b9b4b2,#e9e6e4 50%,#9c9693)" role="img" aria-label="Young baseball batter in a striped helmet"></div>
    <div class="hero-panel" style="width:128px;background:linear-gradient(180deg,#7f95a8 0%,#2d5c86 40%,#2f6e28 100%)" role="img" aria-label="Boy kicking a football in a stadium"></div>
    <div class="hero-panel" style="width:128px;background:linear-gradient(180deg,#b9c0c6 0%,#c99a6e 50%,#a83a2a 100%)" role="img" aria-label="Tennis player with racket raised"></div>
    <div class="hero-panel" style="width:120px;background:linear-gradient(180deg,#c9b7a4 0%,#d9cfc5 50%,#b6b2ad 100%)" role="img" aria-label="Girls reaching for a basketball above the hoop"></div>
    <svg class="arrow" style="left:21px" viewBox="0 0 24 24"><circle cx="12" cy="12" r="10.5" fill="rgba(0,0,0,.25)" stroke="#fff" stroke-width="1.6"/><path d="M14 7l-5 5 5 5" fill="none" stroke="#fff" stroke-width="2"/></svg>
    <svg class="arrow" style="left:706px" viewBox="0 0 24 24"><circle cx="12" cy="12" r="10.5" fill="rgba(0,0,0,.25)" stroke="#fff" stroke-width="1.6"/><path d="M10 7l5 5-5 5" fill="none" stroke="#fff" stroke-width="2"/></svg>
  </section>

  <section class="band">
    <div class="band-copy"><div class="l1">Looking for a new ways to increase</div><div class="l2">revenue and awareness to your students?</div></div>
  </section>
  <div class="btn btn-book">Book Online</div>
  <div class="btn btn-cal">Training Calendar</div>

  <section class="tips">
    <svg class="abs" style="left:0;top:380px" width="749" height="279" viewBox="0 0 749 279">
      <polygon points="406,0 749,0 749,279 406,279 470,190 470,60" fill="var(--blue)"/>
      <path d="M283 58V34h24" fill="none" stroke="var(--lime)" stroke-width="3"/>
      <path d="M283 197v24h24" fill="none" stroke="var(--lime)" stroke-width="3"/>
      <path d="M698 58V34h-24" fill="none" stroke="#fff" stroke-width="3"/>
      <path d="M698 197v24h-24" fill="none" stroke="#fff" stroke-width="3"/>
    </svg>
    <div class="abs" style="left:300px;top:431px;width:382px;height:176px;background:linear-gradient(120deg,#6f7a62 0%,#c8cdbf 45%,#f4f2ea 60%,#6b665d 100%)" role="img" aria-label="Coach resting a hand on a young athlete's shoulder outdoors"></div>
    <svg class="abs" style="left:300px;top:583px" width="382" height="24" viewBox="0 0 382 24">
      <rect width="382" height="24" fill="rgba(0,0,0,.35)"/>
      <line x1="20" y1="5" x2="362" y2="5" stroke="rgba(255,255,255,.4)" stroke-width="1"/>
      <line x1="20" y1="5" x2="30" y2="5" stroke="#e33" stroke-width="1.5"/>
      <rect x="22" y="11" width="2" height="6" fill="#fff"/><rect x="26" y="11" width="2" height="6" fill="#fff"/>
      <path d="M37 11l4 3-4 3z" fill="#fff"/><rect x="42" y="11" width="1.2" height="6" fill="#fff"/>
      <path d="M54 12h2l3-2v8l-3-2h-2z" fill="#fff"/>
      <text x="66" y="16.5" font-size="5" fill="#ccc" font-family="Arimo,sans-serif">0:11 / 4:05</text>
      <circle cx="317" cy="14" r="2.5" fill="#fff"/>
      <rect x="327" y="11" width="8" height="6" fill="none" stroke="#fff"/><rect x="331" y="13.5" width="3" height="2.5" fill="#fff"/>
      <rect x="341" y="11" width="8" height="5" fill="none" stroke="#fff"/>
      <path d="M355 11h2M355 11v2M362 11h-2M362 11v2M355 17h2M355 17v-2M362 17h-2M362 17v-2" stroke="#fff" stroke-width="1"/>
    </svg>
    <div class="tips-title"><div class="kicker">Video tips from the</div><div class="head">Best Coaches</div></div>
    <p class="tips-text">Lorem ipsum dolor sit amet, consectetur adipiscing elit.<br>Suspendisse id sagittis purus, et posuere ex. Vivamus<br>pharetra ut eros eget tincidunt. Morbi at risus eu erat lob-<br>ortis fermentum.</p>
    <div class="btn-more green">More Info</div>
  </section>

  <section class="grid">
    <div role="img" aria-label="Coach with a basketball in front of seated girls in a gym" style="background:linear-gradient(180deg,#b49a7c 0%,#c8ad8c 45%,#c23a2e 100%)"></div>
    <div class="tile t-red"><h3 style="font-size:13px">Training Diary</h3><p>consectetur adipiscing elasdf<br>purus commodo id dolor Lorem ipsum<br>dolor sit amet, consectetur adipiscing<br>elasdf purus.</p><div class="btn-more">More Info</div></div>
    <div role="img" aria-label="Youth football team in yellow kits in a huddle" style="background:linear-gradient(180deg,#8fa06c 0%,#d9b530 45%,#e2b91e 100%)"></div>
    <div class="tile t-yellow"><h3>Student organisation</h3><p>adipiscing elasdf purus commodo id<br>dolor Lorem ipsum dolor sit amet, con-<br>sectetur adipiscing elasdf purus com-<br>modo id dolor.</p><div class="btn-more">More Info</div></div>
    <div class="tile t-taupe"><h3 style="font-weight:400;font-size:12px">Online lessons</h3><p>adipiscing elasdf purus commodo id<br>dolor Lorem ipsum dolor sit amet, con-<br>sectetur adipiscing elasdf purus com-<br>modo id dolor Lorem .</p><div class="btn-more">More Info</div></div>
    <div role="img" aria-label="Woman in sportswear sitting on a mat with a tablet" style="background:linear-gradient(180deg,#f4f4f4 0%,#e6e6e8 60%,#a9a3b2 100%)"></div>
    <div class="tile t-sand"><h3>Online payment<br>Voucher</h3><p>adipiscing elasdf purus commodo id<br>dolor Lorem ipsum dolor sit amet, con-<br>sectetur adipiscing elasdf.</p><div class="btn-more">More Info</div></div>
    <div style="background:linear-gradient(180deg,#66615c,#555049);position:relative">
      <div role="img" aria-label="Gift voucher card tied with a red ribbon" style="position:absolute;left:15px;top:45px;width:134px;height:64px;background:linear-gradient(120deg,#f3ece3 0%,#efe3d8 55%,#d8372f 75%,#efe3d8 90%)"></div>
    </div>
  </section>

  <footer class="footer">
    <div class="brand" style="top:33px"><span class="brand-dot"></span><span class="brand-name">trellopace</span></div>
    <div class="fcol" style="left:249px"><h4>Information</h4>About Trellopace<br>Imprint<br>Contact</div>
    <div class="fcol" style="left:420px"><h4>Links</h4>Terms and conditions<br>Terms and conditions for Pros<br>Terms and conditions Pro Teams</div>
    <span class="social" style="left:632px"></span>
    <span class="social" style="left:662px"></span>
  </footer>

</div>
</body>
</html>
```